NEW HIP COOL PROGRESSIVE FUN PPE BUSINESS IN NEED OF STANDOUT ADS

Design a banner ad that is cool, hip, and happening related to PPE. We have a healthcare business that is uber conservative and we have all the "proper" and dull ads to represent the seriousness of our true mission and passion. tidelumo.com is an e-commerce non-medical PPE business based in Hawaii. We are ready to share our brand with more people online. Help us create something fun and progressive. Get inspiration from our under construction e-commerce store....tidelumo.com
Updates

Low design quality

Target Market(s)

BUSINESSES IN NEED OF PPE OPENING UP, FAMILIES AND INDIVIDUALS IN NEED OF PPE, SCHOOLS IN NEED OF PPE.

Industry/Entity Type

Medical Supply

Font styles to use
Serif
Sans Serif

Requirements
Must have
• Add some hawaiian or local flair. Don't make it look so clinical. This is a site for consumers and businesses.

```html
<!DOCTYPE html>
<html lang="en">
<head>
<meta charset="UTF-8">
<title>Tidelumo – Protect Yourself and Your Family</title>
<link rel="stylesheet" href="https://fonts.googleapis.com/css2?family=Oswald:wght@600&family=Poppins:wght@400;500;600&display=swap">
<style>
  :root {
    --mountain-dark: #2c4524;
    --mountain: #46662f;
    --jungle-bright: #6f9a34;
    --sand: #d8cba2;
    --foam: #c9ddd6;
    --sea-light: #6fb8ad;
    --sea-deep: #2a7f7a;
    --panel: rgba(20, 178, 134, 0.93);
    --white: #ffffff;
    --ink-grey: #555555;
    --brand-green: #1f8a3a;
    --icon-green: #2fb45a;
    --suit-blue: #9fd3e4;
  }
  * { margin: 0; padding: 0; box-sizing: border-box; }
  html, body { width: 1200px; height: 500px; overflow: hidden; background: var(--white); }
  .banner { position: relative; width: 1200px; height: 500px; overflow: hidden; }
  .coast-photo {
    position: absolute; inset: 0;
    background:
      radial-gradient(ellipse 520px 180px at 620px 60px, rgba(44,69,36,0.55), transparent 70%),
      radial-gradient(ellipse 300px 120px at 380px 230px, rgba(111,154,52,0.55), transparent 75%),
      radial-gradient(ellipse 260px 160px at 60px 330px, rgba(225,236,232,0.6), transparent 75%),
      radial-gradient(ellipse 200px 70px at 640px 340px, rgba(111,200,185,0.55), transparent 75%),
      linear-gradient(197deg,
        var(--mountain-dark) 0%,
        var(--mountain) 25%,
        var(--jungle-bright) 46%,
        #5d7f33 51%,
        var(--sand) 54%,
        var(--sand) 58%,
        var(--foam) 62%,
        var(--sea-light) 76%,
        var(--sea-deep) 100%);
  }
  .offer-panel {
    position: absolute; left: 709px; top: 15px; width: 475px; height: 469px;
    background: var(--panel);
  }
  .headline {
    position: absolute; left: 18px; top: 26px;
    font-family: "Oswald", "Arial Narrow", sans-serif; font-weight: 600;
    font-size: 51px; line-height: 53px; color: var(--white); letter-spacing: 1px;
  }
  .tagline {
    position: absolute; left: 19px; top: 245px;
    font-family: "Poppins", Arial, sans-serif; font-weight: 500;
    font-size: 17.5px; line-height: 22.5px; color: var(--white); letter-spacing: 0.6px;
  }
  .shop-button {
    position: absolute; left: 19px; top: 308px; width: 150px; height: 38px;
    background: var(--white); color: var(--ink-grey);
    font-family: "Poppins", Arial, sans-serif; font-size: 14px; font-weight: 400;
    display: flex; align-items: center; justify-content: center; text-decoration: none;
  }
  .suit-figure {
    position: absolute; left: 322px; top: 32px; width: 128px; height: 297px;
    background: linear-gradient(180deg, var(--suit-blue) 0%, var(--white) 12%, var(--white) 88%, var(--suit-blue) 100%);
    border-radius: 40px 40px 10px 10px; opacity: 0.95;
  }
  .product-icons { position: absolute; left: 24px; top: 384px; display: flex; gap: 8px; }
  .product-icons svg { width: 51px; height: 51px; filter: drop-shadow(1px 2px 1px rgba(0,0,0,0.2)); }
  .brand-corner { position: absolute; left: 0; bottom: 0; width: 210px; height: 130px; }
  .brand-name {
    position: absolute; left: 16px; bottom: 26px;
    font-family: "Poppins", Arial, sans-serif; font-weight: 600;
    font-size: 23px; color: var(--ink-grey); letter-spacing: -0.5px;
  }
</style>
</head>
<body>
<div class="banner">
  <div class="coast-photo" role="img" aria-label="Aerial photo of a green Hawaiian mountain coastline with sandy beach and turquoise sea"></div>

  <div class="offer-panel">
    <h1 class="headline">PROTECT<br>YOURSELF<br>AND YOUR<br>FAMILY</h1>
    <p class="tagline">HAWAII’S TRUSTED HEALTH<br>CARE COMPANY FOR 25 YEARS</p>
    <a class="shop-button" href="#">SHOP NOW</a>
    <div class="suit-figure" role="img" aria-label="Illustration of a person in a white protective suit, face shield and blue gloves"></div>

    <div class="product-icons">
      <svg viewBox="0 0 52 52" aria-label="Gloves"><circle cx="26" cy="26" r="24" fill="var(--white)" stroke="var(--brand-green)" stroke-width="2"/><path d="M16 36 L14 22 L18 22 L19 16 L22 16 L23 22 L27 32 Z M26 38 L30 20 L33 20 L34 14 L37 14 L38 24 L36 38 Z" fill="var(--icon-green)"/></svg>
      <svg viewBox="0 0 52 52" aria-label="Sanitizer spray"><circle cx="26" cy="26" r="24" fill="var(--white)" stroke="var(--brand-green)" stroke-width="2"/><rect x="21" y="22" width="11" height="17" rx="2" fill="var(--icon-green)"/><rect x="23" y="14" width="7" height="8" fill="var(--icon-green)"/><path d="M16 14 L22 16" stroke="var(--icon-green)" stroke-width="2"/></svg>
      <svg viewBox="0 0 52 52" aria-label="Face mask"><circle cx="26" cy="26" r="24" fill="var(--white)" stroke="var(--brand-green)" stroke-width="2"/><path d="M15 21 Q26 16 37 21 L36 30 Q26 37 16 30 Z" fill="var(--icon-green)"/><path d="M15 23 Q9 26 16 29 M37 23 Q43 26 36 29" stroke="var(--icon-green)" stroke-width="1.5" fill="none"/></svg>
      <svg viewBox="0 0 52 52" aria-label="Face shield"><circle cx="26" cy="26" r="24" fill="var(--white)" stroke="var(--brand-green)" stroke-width="2"/><rect x="17" y="14" width="18" height="5" rx="2" fill="var(--brand-green)"/><rect x="17" y="19" width="18" height="19" rx="3" fill="var(--icon-green)" opacity="0.8"/></svg>
      <svg viewBox="0 0 52 52" aria-label="Wipes"><circle cx="26" cy="26" r="24" fill="var(--white)" stroke="var(--brand-green)" stroke-width="2"/><path d="M13 28 L25 22 L39 26 L39 34 L26 38 L13 34 Z" fill="var(--icon-green)"/><circle cx="19" cy="18" r="3" fill="var(--icon-green)"/></svg>
      <svg viewBox="0 0 52 52" aria-label="Protective suit"><circle cx="26" cy="26" r="24" fill="var(--white)" stroke="var(--brand-green)" stroke-width="2"/><circle cx="26" cy="14" r="4" fill="var(--icon-green)"/><path d="M20 19 L32 19 L35 31 L32 31 L31 40 L27 40 L26 31 L25 40 L21 40 L20 31 L17 31 Z" fill="var(--icon-green)"/></svg>
    </div>
  </div>

  <svg class="brand-corner" viewBox="0 0 210 130" aria-hidden="true">
    <path d="M0 6 Q70 -6 125 12 Q190 40 210 130 L0 130 Z" fill="var(--brand-green)"/>
    <path d="M0 6 Q65 -4 118 14 Q178 42 200 130 L0 130 Z" fill="var(--white)"/>
  </svg>
  <div class="brand-name">tidelumo.com</div>
</div>
</body>
</html>
```